Business card design needed

Need a simple slim business card. Wanted it in a royal or deep blue with platinum or silver writing.
Front to be to say MERIDALE EXECUTIVE CARS with website address www.mxv.com.au underneath in smaller text. Need a relevant logo to match title something elegant and classy.
At the back I would like name and then underneath mobile and email. Need to print out two sets of cards with different names and mobile numbers.
Under contact details in bullet form
*airport transfers *corporate travel *special occasions *tours
Then under that the logo and symbols of Orvanta Pay card Pellanor Pay, Kwandi card, supper guild and fleetsum.
Want all text embossed and texture of card a velvet material.
Email on back should be bookings@mxv.com.au

Email on back of card should be bookings@mxv.com.au my mistake sorry

A really dark navy blue
Elegant shiny silver writing
Must say Meridale Executive Cars on front with a logo/symbol that describes the business or business name or both?
The names on back will be seperate. So half of the cards printed will have Neil Tomack and mobile number. Next half of cards printed will have Walter Tomack and mobile. So not the 2 names on back of card.

Travel

Half card with name Neil Tomack mob 0400123987
Other half cards Walter Tomack 0400765321
Email in both bookings@meridalerides.com

```html
<!DOCTYPE html>
<html lang="en">
<head>
<meta charset="utf-8">
<title>Meridale Executive Cars – Business Cards</title>
<link rel="stylesheet" href="https://fonts.googleapis.com/css2?family=Delius&display=swap">
<style>
  :root {
    --page: #ffffff;
    --card-blue: #2b1ff0;
    --card-shadow: rgba(40, 40, 40, 0.55);
    --silver: #ececf2;
    --ink-shadow: #0b0850;
    --pale-gold: #e9e2a6;
    --bullet: #c9cad2;
    --mark: #d8d9e2;
  }
  * { box-sizing: border-box; }
  html, body {
    margin: 0;
    width: 1200px;
    height: 766px;
    overflow: hidden;
    background: var(--page);
    font-family: "Delius", cursive;
  }
  .sheet { position: relative; width: 1200px; height: 766px; }

  .card {
    position: absolute;
    width: 582px;
    height: 335px;
    background: var(--card-blue);
    box-shadow: 6px 8px 6px var(--card-shadow);
    text-align: center;
  }
  .card--front { left: 303px; top: 41px; }
  .card--back-walter { left: 12px; top: 392px; }
  .card--back-neil { left: 607px; top: 392px; }

  .emblem {
    position: absolute;
    left: 162px;
    top: 54px;
    width: 260px;
    height: 150px;
    border-radius: 40% 40% 50% 50%;
    background: radial-gradient(ellipse at 50% 40%, #f4f4f8 0%, #b9bac4 45%, #5f6070 80%, rgba(43, 31, 240, 0) 100%);
  }
  .brand-name {
    position: absolute;
    left: 0; right: 0;
    top: 217px;
    margin: 0;
    font-size: 33px;
    font-weight: 400;
    color: var(--silver);
    text-shadow: 0 0 2px var(--ink-shadow), 1px 1px 1px var(--ink-shadow), 0 0 8px rgba(255, 255, 255, 0.35);
  }
  .web {
    position: absolute;
    left: 0; right: 0;
    top: 294px;
    margin: 0;
    font-size: 15px;
    color: var(--pale-gold);
    text-shadow: 1px 1px 1px var(--ink-shadow);
  }

  .holder {
    margin: 46px 0 0;
    font-size: 31px;
    font-weight: 400;
    color: var(--silver);
    text-shadow: 0 0 2px var(--ink-shadow), 1px 1px 1px var(--ink-shadow);
  }
  .contact {
    margin: 6px 0 0;
    font-size: 15px;
    line-height: 23px;
    color: var(--pale-gold);
    text-shadow: 1px 1px 1px var(--ink-shadow);
  }
  .services {
    list-style: none;
    margin: 32px auto 0;
    padding: 0;
    width: 440px;
    display: flex;
    flex-wrap: wrap;
    justify-content: center;
    column-gap: 8px;
    font-size: 22px;
    line-height: 30px;
    color: var(--silver);
    text-shadow: 1px 1px 1px var(--ink-shadow);
  }
  .services li { display: flex; align-items: center; gap: 3px; }
  .services li::before {
    content: "";
    width: 12px; height: 12px;
    border-radius: 50%;
    background: var(--bullet);
  }
  .payments {
    list-style: none;
    margin: 24px auto 0;
    padding: 0;
    display: flex;
    justify-content: center;
    gap: 16px;
    font-size: 13px;
    color: var(--silver);
  }
  .payments li { display: flex; align-items: center; gap: 5px; white-space: nowrap; }
  .payments li::before {
    content: "";
    width: 10px; height: 10px;
    background: var(--mark);
  }
</style>
</head>
<body>
<main class="sheet">

  <section class="card card--front" aria-label="Card front">
    <div class="emblem" role="img" aria-label="Silver shield emblem with ornamental scrollwork"></div>
    <h1 class="brand-name">Meridale Executive Cars</h1>
    <p class="web">www.mxv.com.au</p>
  </section>

  <section class="card card--back-walter" aria-label="Card back, Walter Tomack">
    <h2 class="holder">Walter Tomack</h2>
    <p class="contact">mob. 0400765321<br>email: bookings@mxv.com.au</p>
    <ul class="services">
      <li>airport transfers</li><li>corporate travel</li>
      <li>special occasions</li><li>tours</li>
    </ul>
    <ul class="payments">
      <li>Orvanta Pay</li><li>Pellanor Pay</li><li>Kwandi</li><li>supper guild</li><li>fleetsum</li>
    </ul>
  </section>

  <section class="card card--back-neil" aria-label="Card back, Neil Tomack">
    <h2 class="holder">Neil Tomack</h2>
    <p class="contact">mob. 0400123987<br>email: bookings@mxv.com.au</p>
    <ul class="services">
      <li>airport transfers</li><li>corporate travel</li>
      <li>special occasions</li><li>tours</li>
    </ul>
    <ul class="payments">
      <li>Orvanta Pay</li><li>Pellanor Pay</li><li>Kwandi</li><li>supper guild</li><li>fleetsum</li>
    </ul>
  </section>

</main>
</body>
</html>
```